Android App Design Project

Hi my name is Keril, and I'm an android developer. I'm searching for a professional designer that can design my app.I have already launched the app and you can find it in the appora depot.

Main Requirements
- 15 sport icons
- 6 android pages
- Action bar
- Buttons and other icons

You need to do all requirements to submit a design. I need the design in both JPEG format and Photoshop PSD format. If you are interested then please download the PDF file ,it will help you a lot.
The name of the app is "MATCH VUE Prime" you can find it in Appora Shelf.

NOTICE: You might read that the Payment is not guaranteed if I'm not happy with the design BUT if you make a good design and you win the contest, then you become my main designer that means if I want to change or add something to the design of the app in the future I return to you "the winner" directly to make the redesign and get paid for it.

Regards.
Skype: Idun marvelo "idun47"
E-mail: idunkeril@mailvox.test

Industry/Entity Type

Tv

Requirements
Must have
• - 15 sport icons
- 6 android pages
- Action bar
- Buttons and other icons

```html
<!DOCTYPE html>
<html lang="en">
<head>
<meta charset="utf-8">
<title>Match Vue Prime – Splash</title>
<link href="https://fonts.googleapis.com/css2?family=Ubuntu+Condensed&family=Ubuntu:wght@500&display=swap" rel="stylesheet">
<style>
  :root {
    --bar-top: #f4874a;
    --bar-bottom: #e2672a;
    --bar-edge: #8a3a12;
    --button-face: #d9592a;
    --button-edge: #a8431c;
    --ink-light: #ffffff;
    --screen-center: #6e6e6e;
    --screen-edge: #565656;
    --divider-dark: #4a4a4a;
    --divider-light: #787878;
    --brand-ink: #f2f2ee;
  }
  html, body {
    margin: 0;
    padding: 0;
    width: 817px;
    height: 1200px;
    overflow: hidden;
  }
  .app-screen {
    position: relative;
    width: 817px;
    height: 1200px;
    background: radial-gradient(ellipse 70% 55% at 50% 45%, var(--screen-center), var(--screen-edge));
    font-family: "Ubuntu Condensed", "Arial Narrow", sans-serif;
  }
  .action-bar {
    position: absolute;
    left: 0; top: 0;
    width: 100%;
    height: 100px;
    background: linear-gradient(to bottom, var(--bar-top), var(--bar-bottom));
    border-bottom: 3px solid var(--bar-edge);
    display: flex;
    align-items: center;
    justify-content: center;
  }
  .menu-button {
    position: absolute;
    left: 31px; top: 26px;
    width: 80px; height: 48px;
    border-radius: 10px;
    background: var(--button-face);
    border: 2px solid var(--button-edge);
    box-sizing: border-box;
    display: flex;
    align-items: center;
    justify-content: center;
  }
  .screen-title {
    margin: 0;
    color: var(--ink-light);
    font-family: "Ubuntu", sans-serif;
    font-weight: 500;
    font-size: 52px;
    letter-spacing: -1px;
    transform: scaleX(0.85);
  }
  .brand-name {
    position: absolute;
    left: 0; top: 530px;
    width: 100%;
    text-align: center;
    margin: 0;
    color: var(--brand-ink);
    font-size: 78px;
    letter-spacing: 2px;
  }
  .divider {
    position: absolute;
    left: 115px; top: 913px;
    width: 562px; height: 0;
    border-top: 2px solid var(--divider-dark);
    border-bottom: 1px solid var(--divider-light);
  }
  .loading-spinner {
    position: absolute;
    left: 353px; top: 994px;
    width: 96px; height: 96px;
  }
</style>
</head>
<body>
  <main class="app-screen">
    <header class="action-bar">
      <div class="menu-button" aria-label="Menu">
        <svg width="36" height="26" viewBox="0 0 36 26" aria-hidden="true">
          <rect x="0" y="1" width="36" height="5" rx="1" fill="#fff"/>
          <rect x="0" y="10.5" width="36" height="5" rx="1" fill="#fff"/>
          <rect x="0" y="20" width="36" height="5" rx="1" fill="#fff"/>
        </svg>
      </div>
      <h1 class="screen-title">Match Vue Prime</h1>
    </header>

    <p class="brand-name">MATCH VUE PRIME</p>

    <div class="divider"></div>

    <svg class="loading-spinner" viewBox="-50 -50 100 100" role="img" aria-label="Loading">
      <g stroke-width="8" stroke-linecap="round">
        <line x1="0" y1="-22" x2="0" y2="-40" stroke="#f4f4f4" opacity="1"/>
        <line x1="0" y1="-22" x2="0" y2="-40" stroke="#f4f4f4" opacity="0.92" transform="rotate(30)"/>
        <line x1="0" y1="-22" x2="0" y2="-40" stroke="#f4f4f4" opacity="0.84" transform="rotate(60)"/>
        <line x1="0" y1="-22" x2="0" y2="-40" stroke="#e8e8e8" opacity="0.76" transform="rotate(90)"/>
        <line x1="0" y1="-22" x2="0" y2="-40" stroke="#dcdcdc" opacity="0.68" transform="rotate(120)"/>
        <line x1="0" y1="-22" x2="0" y2="-40" stroke="#cfcfcf" opacity="0.6" transform="rotate(150)"/>
        <line x1="0" y1="-22" x2="0" y2="-40" stroke="#bdbdbd" opacity="0.52" transform="rotate(180)"/>
        <line x1="0" y1="-22" x2="0" y2="-40" stroke="#a8a8a8" opacity="0.46" transform="rotate(210)"/>
        <line x1="0" y1="-22" x2="0" y2="-40" stroke="#8f8f8f" opacity="0.42" transform="rotate(240)"/>
        <line x1="0" y1="-22" x2="0" y2="-40" stroke="#444" opacity="0.7" transform="rotate(270)"/>
        <line x1="0" y1="-22" x2="0" y2="-40" stroke="#333" opacity="0.8" transform="rotate(300)"/>
        <line x1="0" y1="-22" x2="0" y2="-40" stroke="#2a2a2a" opacity="0.9" transform="rotate(330)"/>
      </g>
    </svg>
  </main>
</body>
</html>
```